Business Cards for Tomas and Welby

Design of business cards for two people with the recently created brand Caldor Mobile. Caldor Mobile wants to become a worldwide major player on the secondhand phone market. It gathers send hand phones from individuals, refurbish them and sell them throughout the world. It has a green impact (recycling) and we also contribute to social project in Africa (a percentage of our benefits are sent to build school, sport facilities, etc.

Target Market(s)

B2B - Tomas and Welby are in contact with distributors across Africa.

Industry/Entity Type

Wireless Communication

Contact Information for Business Card

Tomas Vireaux
Head of Emerging Markets
Caldor Energy South Africa (Pty) Ltd
Fennick Street 47
2031 Sandton - Johannesburg
South Africa
Tel: + 27 10 555 0184
Mobile : +27 82 55 017
Email : tomas.vireaux@caldormobile.example
Skype: tomas.vireaux
Web: www.caldormobile.example
 

Welby Crofts
Head of Southern Africa
Fennick Street 47
South Africa
Tel: + 27 10 555 0184
Mobile: +27 83 555 0297
Email: welby.crofts@caldormobile.example
Skype: welby.crofts
Web: www.caldormobile.example

Requirements
Must have
• The cards need to be "serious", trustable, with a worldwide presence.
Nice to have
• Some "green" / recycling touch would be nice but not necessary if in contradiction with the general design.

```html
<!DOCTYPE html>
<html lang="en">
<head>
<meta charset="utf-8">
<title>Caldor Mobile – Business Cards</title>
<link rel="stylesheet" href="https://fonts.googleapis.com/css2?family=Roboto:wght@400;500;700&display=swap">
<style>
  :root {
    --backdrop: #e4e4e4;
    --card-white: #ffffff;
    --navy: #0f2e4b;
    --brand-blue: #2f90d6;
    --text-navy: #13314f;
    --divider: rgba(255,255,255,0.28);
  }
  * { box-sizing: border-box; margin: 0; padding: 0; }
  html, body {
    width: 1200px; height: 900px; overflow: hidden;
    background: var(--backdrop);
    font-family: "Roboto", Arial, sans-serif;
  }
  .card {
    position: absolute; top: 130px;
    width: 400px; height: 640px;
    background: var(--card-white);
    box-shadow: 0 6px 18px rgba(0,0,0,0.18);
    overflow: hidden;
  }
  .card-tomas { left: 170px; }
  .card-welby { left: 630px; }
  .brand {
    position: absolute; top: 110px; left: 0; width: 100%;
    text-align: center;
  }
  .brand-mark {
    display: block; width: 36px; height: 36px; margin: 0 auto 16px;
    background: var(--brand-blue); border-radius: 50%;
  }
  .brand-name {
    display: block;
    font-size: 32px; line-height: 38px; font-weight: 700;
    color: var(--text-navy); letter-spacing: -0.3px;
  }
  .company {
    position: absolute; top: 228px; left: 0; width: 100%;
    text-align: center; color: var(--text-navy);
    font-size: 18px; line-height: 23px;
  }
  .tab {
    position: absolute; left: 60px; right: 8px; top: 290px; height: 40px;
    background: var(--brand-blue); border-radius: 18px 18px 0 0;
  }
  .contact-panel {
    position: absolute; left: 0; right: 0; top: 312px; bottom: 0;
    background: var(--navy); color: #fff;
  }
  .timeline { position: absolute; left: 0; top: 0; }
  .field { position: absolute; left: 100px; right: 14px; white-space: nowrap; }
  .person-name { top: 18px; font-size: 26px; line-height: 30px; font-weight: 400; letter-spacing: 0.3px; }
  .person-name strong { font-weight: 700; }
  .person-title { top: 52px; font-size: 16px; line-height: 20px; }
  .address, .phones, .web { font-size: 15px; line-height: 20px; }
  .address { top: 100px; }
  .phones { top: 166px; }
  .web { top: 232px; }
  .rule { position: absolute; left: 100px; right: 24px; height: 1px; background: var(--divider); }
  .rule-1 { top: 86px; }
  .rule-2 { top: 152px; }
  .rule-3 { top: 218px; }
</style>
</head>
<body>
  <article class="card card-tomas">
    <div class="brand">
      <span class="brand-mark"></span>
      <span class="brand-name">CaldorMobile</span>
    </div>
    <p class="company">Caldor Energy<br>South Africa (Pty) Ltd</p>
    <div class="tab"></div>
    <section class="contact-panel">
      <svg class="timeline" width="100" height="328" viewBox="0 0 100 328">
        <line x1="60" y1="16" x2="60" y2="300" stroke="#2f90d6" stroke-width="3"/>
        <circle cx="60" cy="50" r="15" fill="#2f90d6"/>
        <circle cx="60" cy="45" r="4" fill="#fff"/>
        <path d="M52 58 q8 -9 16 0 z" fill="#fff"/>
        <circle cx="60" cy="120" r="15" fill="#2f90d6"/>
        <path d="M60 129 l-6 -8 a7 7 0 1 1 12 0 z" fill="#fff"/>
        <circle cx="60" cy="116" r="2.5" fill="#2f90d6"/>
        <circle cx="60" cy="186" r="15" fill="#2f90d6"/>
        <path d="M55 178 h3 l1 5 -2.5 1.5 q1.5 4 5 6 l1.5 -2.5 5 1 v3 q-1 2.5 -3.5 2 q-10 -2.5 -12.5 -12.5 q0 -3.5 2.5 -3.5 z" fill="#fff"/>
        <circle cx="60" cy="252" r="15" fill="#2f90d6"/>
        <g fill="none" stroke="#fff" stroke-width="1.4">
          <circle cx="60" cy="252" r="8"/>
          <ellipse cx="60" cy="252" rx="3.5" ry="8"/>
          <line x1="52" y1="252" x2="68" y2="252"/>
        </g>
      </svg>
      <h1 class="field person-name"><strong>TOMAS</strong> VIREAUX</h1>
      <p class="field person-title">Head of Emerging Markets</p>
      <div class="rule rule-1"></div>
      <p class="field address">Fennick Street 47, 2031 Sandton -<br>Johannesburg, South Africa</p>
      <div class="rule rule-2"></div>
      <p class="field phones">+27 10 555 0184<br>+27 82 55 017</p>
      <div class="rule rule-3"></div>
      <p class="field web">tomas.vireaux@caldormobile.example<br>www.caldormobile.example</p>
    </section>
  </article>

  <article class="card card-welby">
    <div class="brand">
      <span class="brand-mark"></span>
      <span class="brand-name">CaldorMobile</span>
    </div>
    <p class="company">Caldor Energy<br>South Africa (Pty) Ltd</p>
    <div class="tab"></div>
    <section class="contact-panel">
      <svg class="timeline" width="100" height="328" viewBox="0 0 100 328">
        <line x1="60" y1="16" x2="60" y2="300" stroke="#2f90d6" stroke-width="3"/>
        <circle cx="60" cy="50" r="15" fill="#2f90d6"/>
        <circle cx="60" cy="45" r="4" fill="#fff"/>
        <path d="M52 58 q8 -9 16 0 z" fill="#fff"/>
        <circle cx="60" cy="120" r="15" fill="#2f90d6"/>
        <path d="M60 129 l-6 -8 a7 7 0 1 1 12 0 z" fill="#fff"/>
        <circle cx="60" cy="116" r="2.5" fill="#2f90d6"/>
        <circle cx="60" cy="186" r="15" fill="#2f90d6"/>
        <path d="M55 178 h3 l1 5 -2.5 1.5 q1.5 4 5 6 l1.5 -2.5 5 1 v3 q-1 2.5 -3.5 2 q-10 -2.5 -12.5 -12.5 q0 -3.5 2.5 -3.5 z" fill="#fff"/>
        <circle cx="60" cy="252" r="15" fill="#2f90d6"/>
        <g fill="none" stroke="#fff" stroke-width="1.4">
          <circle cx="60" cy="252" r="8"/>
          <ellipse cx="60" cy="252" rx="3.5" ry="8"/>
          <line x1="52" y1="252" x2="68" y2="252"/>
        </g>
      </svg>
      <h1 class="field person-name"><strong>WELBY</strong> CROFTS</h1>
      <p class="field person-title">Head of Southern Africa</p>
      <div class="rule rule-1"></div>
      <p class="field address">Fennick Street 47, 2031 Sandton -<br>Johannesburg, South Africa</p>
      <div class="rule rule-2"></div>
      <p class="field phones">+27 10 555 0184<br>+27 83 555 0297</p>
      <div class="rule rule-3"></div>
      <p class="field web">welby.crofts@caldormobile.example<br>www.caldormobile.example</p>
    </section>
  </article>
</body>
</html>
```